Redesign of my Homepage - Online resource for anyone to learn American Sign Language

I would like to have a new homepage design http://www.SignPathora.com . My business is a website for anyone to learn American Sign Language. There are over 300 video lessons, with each lesson having 20 vocabulary words, retention exercises, 16,000 video dictionary etc. It is a very extensive site. It is a self paced website. If you need a log in to see what customers see, please let me know. I would like to keep the same color scheme. I want the website to look modern and clean. I want a fresh look! I want something that is easy to navigate, attracts customers, and easy to follow. I would like the final design to communicate that my website is for anyone to learn how to sign with this incredible program.

Target Market(s)

Students taking American Sign Language, Parents with Deaf children, future interpreters for the deaf, co-workers of the Deaf. Also, schools that offer American Sign Language (online schools, homeschools, etc. ).

Industry/Entity Type

Business

Number of Pages Required

1 page

Requirements
Must have
• My project must be very clean and clear. I want my homepage to show that this is a program for people to learn how American Sign Language.
Nice to have
• Not sure. Surprise me.

```html
<!DOCTYPE html>
<html lang="en">
<head>
<meta charset="utf-8">
<title>SignPathora – Our Team</title>
<link href="https://fonts.googleapis.com/css2?family=Open+Sans:wght@400;600;700&display=swap" rel="stylesheet">
<style>
:root{
  --green:#00a032;
  --green-band:#069a30;
  --dark:#3c3c3c;
  --panel:#f2f2f2;
  --text:#444;
  --muted:#666;
  --frame:#dcdcdc;
  --photo:#e3e3e3;
  --field:#f5f5f5;
  --badge:#d6d6d6;
}
*{box-sizing:border-box;margin:0;padding:0}
html,body{width:1059px;height:1200px;overflow:hidden}
body{position:relative;font-family:"Open Sans",Verdana,sans-serif;color:var(--text);
  background:linear-gradient(#fff 0,#e4e4e4 863px,#fff 863px)}
.abs{position:absolute}
.page{left:115px;top:-2px;width:828px;height:1112px;background:#fff;border:2px solid var(--frame);border-top:none;border-radius:0 0 10px 10px}
.team-title{left:0;width:1059px;top:31px;text-align:center;color:var(--green);font-size:23px;letter-spacing:1.5px;font-weight:400}
.team-sub{left:0;width:1059px;top:62px;text-align:center;color:var(--green);font-size:11.5px;letter-spacing:1px}
.photo{width:238px;height:243px;top:109px}
.member{top:380px;width:230px;font-size:10.5px}
.member .name{font-weight:700;font-size:11.5px;color:#333;letter-spacing:.3px}
.member .role{color:var(--green);font-size:11px;margin-top:4px}
.member .line{display:flex;align-items:center;gap:4px;margin-top:9px;color:#555}
.member .line + .line{margin-top:7px}
.icons{display:flex;gap:12px;margin-top:6px}
.dot{width:10px;height:10px;border-radius:50%;background:#444;display:block}
.arrow{top:522px;width:26px;height:26px;background:#ddd;display:flex;align-items:center;justify-content:center}
.touch{left:126px;top:573px;width:804px;height:212px;background:var(--panel)}
.h2{color:var(--green);font-size:21px;letter-spacing:.5px;font-weight:400}
.info{font-size:13px;letter-spacing:.8px;color:#555}
.info b{color:var(--green);font-weight:400}
.signup{font-size:13px;letter-spacing:.8px;color:#555}
.email-box{left:607px;top:676px;width:282px;height:35px;border:1px solid var(--green);background:#fff;font-size:11px;letter-spacing:.8px;color:#777;padding:10px 0 0 16px}
.go{left:852px;top:676px;width:37px;height:35px;background:var(--green);color:#fff;font-size:13px;display:flex;align-items:center;justify-content:center}
.band{left:126px;top:785px;width:804px;height:247px;background:var(--green-band)}
.links{left:160px;top:796px;color:#fff;font-size:12.5px;font-weight:600}
.about{left:159px;top:825px;width:220px;color:#fff;font-size:11.3px;line-height:19.4px;text-align:justify}
.tweets{left:402px;top:826px;width:209px;height:193px;background:#ececec;border-radius:3px;box-shadow:0 2px 0 #bbb;overflow:hidden}
.tweets-head{height:30px;background:linear-gradient(#f3f3f3,#dcdcdc);color:var(--green);font-size:14px;padding:6px 10px;position:relative}
.tweets-head i{position:absolute;right:6px;top:5px;width:22px;height:20px;background:#3aa6e0;border-radius:3px}
.tweet{padding:5px 4px 5px 8px;font-size:9.9px;letter-spacing:-.15px;line-height:13.5px;color:#333;border-bottom:1px solid #d4d4d4;height:67px}
.tweet small{display:block;color:#999;font-size:8px;margin-top:3px}
.tweets-foot{padding:4px 10px;font-size:10.5px;color:#333}
.tweets-foot span{color:#9ab;font-size:10px}
.tweets-foot em{color:#3aa6e0;font-style:normal}
.field{left:634px;width:256px;background:var(--field);border:1px solid #ddd;border-radius:3px;color:#999;font-size:13.5px;padding:7px 9px}
.send{left:634px;top:989px;width:256px;height:33px;background:#c8c8c8;border-radius:3px;color:#777;font-size:14px;display:flex;align-items:center;justify-content:center}
.bottom{left:126px;top:1032px;width:804px;height:68px;background:var(--dark);border-radius:0 0 10px 10px;color:#fff;font-size:13px;display:flex;align-items:center;justify-content:center;letter-spacing:.2px}
</style>
</head>
<body>
<div class="abs page"></div>

<h1 class="abs team-title">OUR TEAM</h1>
<p class="abs team-sub">meet our specialist</p>

<div class="abs photo" style="left:140px;background:linear-gradient(#e4e4e4 55%,#3a2c2c 80%)" role="img" aria-label="Portrait photo of Marcus Ellery, founder"></div>
<div class="abs photo" style="left:409px;background:linear-gradient(#e4e4e4 50%,#4a5a72 80%)" role="img" aria-label="Portrait photo of Julian R, deaf expert"></div>
<div class="abs photo" style="left:678px;background:linear-gradient(#e4e4e4 55%,#222 82%)" role="img" aria-label="Portrait photo of Helen T, deaf expert"></div>

<svg width="0" height="0" style="position:absolute">
  <symbol id="phone" viewBox="0 0 10 10"><path d="M2 1l2 2-1 1.2c.6 1.3 1.5 2.2 2.8 2.8L7 6l2 2-1.2 1.4C4.5 9.2.8 5.5.6 2.2z" fill="#444"/></symbol>
  <symbol id="mail" viewBox="0 0 12 9"><rect x=".5" y=".5" width="11" height="8" fill="none" stroke="#444"/><path d="M.5 .5l5.5 4.5 5.5-4.5" fill="none" stroke="#444"/></symbol>
</svg>

<div class="abs member" style="left:159px">
  <div class="name">Marcus Ellery</div>
  <div class="role">Founder</div>
  <div class="line"><svg width="9" height="9"><use href="#phone"/></svg>: (123) 123-1234</div>
  <div class="line"><svg width="11" height="9"><use href="#mail"/></svg>: marcus@signpathora.com</div>
  <div class="icons"><i class="dot"></i><i class="dot"></i><i class="dot"></i></div>
</div>
<div class="abs member" style="left:415px">
  <div class="name">Julian R</div>
  <div class="role">Deaf expert</div>
  <div class="line"><svg width="9" height="9"><use href="#phone"/></svg>: (123) 123-1234</div>
  <div class="line"><svg width="11" height="9"><use href="#mail"/></svg>: julian@signpathora.com</div>
  <div class="icons"><i class="dot"></i><i class="dot"></i><i class="dot"></i></div>
</div>
<div class="abs member" style="left:702px">
  <div class="name">Helen T</div>
  <div class="role">Deaf expert</div>
  <div class="line"><svg width="9" height="9"><use href="#phone"/></svg>: (123) 123-1234</div>
  <div class="line"><svg width="11" height="9"><use href="#mail"/></svg>: helen@signpathora.com</div>
  <div class="icons"><i class="dot"></i><i class="dot"></i><i class="dot"></i></div>
</div>

<div class="abs arrow" style="left:492px"><svg width="10" height="12"><path d="M7 1L2 6l5 5" fill="none" stroke="#00a032" stroke-width="2.5"/></svg></div>
<div class="abs arrow" style="left:542px"><svg width="10" height="12"><path d="M3 1l5 5-5 5" fill="none" stroke="#00a032" stroke-width="2.5"/></svg></div>

<section class="abs touch"></section>
<h2 class="abs h2" style="left:169px;top:596px">STAY IN TOUCH</h2>
<p class="abs info" style="left:171px;top:645px"><b>ADDRESS :</b> 123 CITY ., PLACE&nbsp; NUM,</p>
<p class="abs info" style="left:171px;top:676px">STRET NAME, 4010</p>
<p class="abs info" style="left:171px;top:706px"><b>PHONE :</b> (555) 204-7781</p>
<p class="abs info" style="left:171px;top:737px"><b>Email :</b> info@signpathora.com</p>

<h2 class="abs h2" style="left:606px;top:596px">NEWSLETTER</h2>
<p class="abs signup" style="left:606px;top:645px">SIGN UP YOUR NEWSLETTER</p>
<div class="abs email-box">EMAIL ADDRESS</div>
<div class="abs go">GO</div>
<svg class="abs" style="left:604px;top:737px" width="170" height="16" aria-label="Social links">
  <circle cx="7" cy="8" r="5.5" fill="#444"/><circle cx="34" cy="8" r="5.5" fill="#444"/>
  <circle cx="64" cy="8" r="5.5" fill="#444"/><circle cx="96" cy="8" r="5.5" fill="#444"/>
  <circle cx="126" cy="8" r="5.5" fill="#444"/><circle cx="154" cy="8" r="5.5" fill="#444"/>
</svg>
<svg class="abs" style="left:785px;top:718px" width="110" height="60" role="img" aria-label="Payment partner badge">
  <line x1="5" y1="58" x2="43" y2="2" stroke="#ddd"/>
  <circle cx="74" cy="29" r="22" fill="var(--badge)"/>
</svg>

<section class="abs band"></section>
<p class="abs links">Contact Us | Our Mission | Terms &amp; Conditions</p>
<p class="abs about">SignPathora is a subscription based website for American Sign Language (ASL) video lessons. The content is for anyone who wishes to learn ASL, regardless of age. It has been designed to instruct deaf students, parents of deaf children, and the community-at-large. You may cancel your subscription at any time. All lessons are taught by Deaf experts of ASL.</p>

<div class="abs tweets">
  <div class="tweets-head">Latest Tweets<i></i></div>
  <div class="tweet">The season of #shoveling has just begun! We think #signlanguage learning is a great way<small>9 mins ago</small></div>
  <div class="tweet">The season of #shoveling has just begun! We think #signlanguage learning is a great way<small>9 mins ago</small></div>
  <div class="tweets-foot">signfeed <span>@signfeed</span> <em>Follow</em></div>
</div>

<div class="abs field" style="top:825px;height:32px">Your name</div>
<div class="abs field" style="top:864px;height:32px">Your mail</div>
<div class="abs field" style="top:903px;height:79px;padding-top:10px">Your message</div>
<div class="abs send">Send</div>

<footer class="abs bottom">SignPathora ©2017 All Rights Reserved | 1485198208.0142s</footer>
</body>
</html>
```